AUSTRALIAN CONSULTING FIRM BUSINESS CARD - MODERN

We are wanting a modern, clean lined business card design. We are professional niche consultancy firm situated in Australia called Marlow Advisory Partners Pty Ltd.
The card should communicate professionalism and creativity and draw on our logo design (attached).
The design should be two sided, landscape orientation.
Target Market(s)
government, not for profit sector, corporate clients
Industry/Entity Type
Landscape
Requirements
Must have
- logo
no new introduced colours

```html
<!DOCTYPE html>
<html lang="en">
<head>
<meta charset="utf-8">
<title>Marlow Advisory Partners – Business Card</title>
<link rel="stylesheet" href="https://fonts.googleapis.com/css2?family=Source+Sans+3:wght@400;600;700&display=swap">
<style>
  :root {
    --brand-blue: #1c4598;
    --brand-purple: #a44a93;
    --accent-cyan: #2a9fd8;
    --card-light: #f7f7f7;
    --card-mid: #e6e6e6;
    --card-front-top: #ececec;
    --card-front-bottom: #d6d6d6;
    --page-bg: #efefef;
  }
  * { box-sizing: border-box; margin: 0; padding: 0; }
  html, body { width: 1200px; height: 750px; overflow: hidden; }
  body {
    background: var(--page-bg);
    font-family: "Source Sans 3", "Myriad Pro", Arial, sans-serif;
  }
  .canvas {
    width: 1200px; height: 750px;
    display: flex; align-items: center; justify-content: center; gap: 40px;
  }
  .card {
    position: relative;
    width: 540px; height: 309px;
    box-shadow: 0 2px 6px rgba(0,0,0,.18);
    overflow: hidden;
  }

  /* Front */
  .card--front {
    background: linear-gradient(160deg, var(--card-front-top), var(--card-front-bottom));
  }
  .wordmark {
    position: absolute; left: 50%; top: 50%;
    transform: translate(-50%, -50%);
    display: flex; align-items: center; gap: 12px;
    color: var(--brand-blue);
  }
  .wordmark__dot {
    width: 18px; height: 18px; border-radius: 50%;
    background: var(--accent-cyan); flex: none;
  }
  .wordmark__name {
    font-weight: 700; line-height: 1.05; text-transform: uppercase;
  }
  .wordmark__name span { display: block; }
  .wordmark__lead { font-size: 38px; letter-spacing: -0.5px; }
  .wordmark__rest { font-size: 13.5px; letter-spacing: 0.4px; }

  /* Back */
  .card--back {
    background: linear-gradient(180deg, var(--card-light), var(--card-mid));
  }
  .card--back .wordmark {
    left: 34px; top: 120px; transform: none; gap: 8px;
  }
  .card--back .wordmark__dot { width: 13px; height: 13px; }
  .card--back .wordmark__lead { font-size: 28px; }
  .card--back .wordmark__rest { font-size: 9.5px; }
  .divider {
    position: absolute; left: 288px; top: 62px;
    width: 1px; height: 110px; background: var(--accent-cyan);
  }
  .contact {
    position: absolute; left: 306px; top: 60px;
  }
  .contact__name {
    color: var(--brand-blue); font-weight: 600; font-size: 19px; line-height: 1.1;
  }
  .contact__role {
    color: var(--brand-purple); font-size: 14px; margin: 2px 0 12px;
  }
  .contact__list { list-style: none; }
  .contact__item {
    display: flex; align-items: center; gap: 8px;
    color: var(--brand-purple); font-size: 12.5px; line-height: 19px;
  }
  .contact__icon { width: 11px; height: 11px; flex: none; fill: var(--brand-blue); }
  .band {
    position: absolute; left: 0; bottom: 0; width: 540px; height: 24px;
  }
</style>
</head>
<body>
<main class="canvas">

  <section class="card card--front" aria-label="Card front">
    <div class="wordmark">
      <span class="wordmark__dot"></span>
      <p class="wordmark__name">
        <span class="wordmark__lead">Marlow</span>
        <span class="wordmark__rest">Advisory Partners Pty Ltd</span>
      </p>
    </div>
  </section>

  <section class="card card--back" aria-label="Card back">
    <div class="wordmark">
      <span class="wordmark__dot"></span>
      <p class="wordmark__name">
        <span class="wordmark__lead">Marlow</span>
        <span class="wordmark__rest">Advisory Partners Pty Ltd</span>
      </p>
    </div>

    <div class="divider"></div>

    <div class="contact">
      <h1 class="contact__name">Elliot Marsh</h1>
      <p class="contact__role">Founder</p>
      <ul class="contact__list">
        <li class="contact__item">
          <svg class="contact__icon" viewBox="0 0 12 12"><path d="M6 0a4 4 0 0 0-4 4c0 3 4 8 4 8s4-5 4-8a4 4 0 0 0-4-4zm0 5.6A1.6 1.6 0 1 1 6 2.4a1.6 1.6 0 0 1 0 3.2z"/></svg>
          No.4 Harbour Lane Perth, Australia
        </li>
        <li class="contact__item">
          <svg class="contact__icon" viewBox="0 0 12 12"><path d="M1 3.5C1 2 2 1.5 6 1.5s5 .5 5 2v1H8.5v-1h-5v1H1zM3 6l1.5-1.5h3L9 6v4.5H3zm3 1a1.3 1.3 0 1 0 0 2.6A1.3 1.3 0 0 0 6 7z"/></svg>
          0412 555 208
        </li>
        <li class="contact__item">
          <svg class="contact__icon" viewBox="0 0 12 12"><path d="M0 2.5h12v7H0zm1 .8v.3l5 3 5-3v-.3z"/></svg>
          info@marlowadvisory.com
        </li>
        <li class="contact__item">
          <svg class="contact__icon" viewBox="0 0 12 12"><path d="M6 .5a5.5 5.5 0 1 0 0 11A5.5 5.5 0 0 0 6 .5zm0 1c.7 0 1.5 1.4 1.7 3.5H4.3C4.5 2.9 5.3 1.5 6 1.5zM1.6 5h1.7a9 9 0 0 1 .5-3A4.5 4.5 0 0 0 1.6 5zm0 2a4.5 4.5 0 0 0 2.2 3 9 9 0 0 1-.5-3zm2.7 0c.2 2.1 1 3.5 1.7 3.5s1.5-1.4 1.7-3.5zm4.4 0a9 9 0 0 1-.5 3 4.5 4.5 0 0 0 2.2-3zm1.7-2a4.5 4.5 0 0 0-2.2-3 9 9 0 0 1 .5 3z"/></svg>
          www.marlowadvisory.com
        </li>
      </ul>
    </div>

    <svg class="band" viewBox="0 0 540 24" preserveAspectRatio="none" aria-hidden="true">
      <polygon points="0,10 330,10 322,24 0,24" fill="var(--brand-blue)"/>
      <polygon points="332,10 540,0 540,24 324,24" fill="var(--brand-purple)"/>
    </svg>
  </section>

</main>
</body>
</html>
```